Brightwave Travel and Tours

Hotel Reservations
Airline Ticketing
Day Tour

My business is a Travel agency. My services are issuing domestic and international tickets. Book room/hotel reservations local/international.
My color preference is apple green/orange/red/blue.
Images of beaches, tickets,luggage.

```html
<!DOCTYPE html>
<html lang="en">
<head>
<meta charset="UTF-8">
<title>Brightwave Travel and Tours – Business Card</title>
<link href="https://fonts.googleapis.com/css2?family=Montserrat:wght@500;600;700&family=Noto+Sans:wght@400;600&display=swap" rel="stylesheet">
<style>
  :root {
    --backdrop: #e9e9e9;
    --card-white: #ffffff;
    --brand-blue: #1d6a8e;
    --band-teal: #1a6f94;
    --swoosh-light: #2f9ad6;
    --swoosh-dark: #1b6890;
    --ink: #1c1c1c;
    --scene-top: #b4dcf3;
    --scene-bottom: #e8eef0;
    --strip-fill: #d3e9f4;
  }
  * { margin: 0; padding: 0; box-sizing: border-box; }
  html, body { width: 1200px; height: 1200px; overflow: hidden; }
  body { background: var(--backdrop); position: relative; font-family: "Noto Sans", sans-serif; }

  .card {
    position: absolute;
    border-radius: 24px;
    overflow: hidden;
    background: var(--card-white);
  }
  .card--front { left: 238px; top: 118px; width: 712px; height: 419px; }
  .card--back  { left: 231px; top: 645px; width: 711px; height: 415px; }

  .scene-placeholder {
    position: absolute; inset: 0;
    background: linear-gradient(180deg, var(--scene-top) 0%, var(--scene-bottom) 100%);
  }

  .brand-mark {
    position: absolute;
    left: 0; right: 0;
    text-align: center;
    font-family: "Montserrat", sans-serif;
    font-weight: 700;
    color: var(--brand-blue);
    line-height: 1;
  }
  .brand-mark__dot {
    display: block;
    margin: 0 auto;
    border-radius: 50%;
    background: var(--brand-blue);
  }
  .brand-mark__name, .brand-mark__tag { display: block; }

  .card--front .brand-mark { top: 150px; }
  .card--front .brand-mark__dot { width: 70px; height: 70px; margin-bottom: 40px; }
  .card--front .brand-mark__name { font-size: 44px; letter-spacing: 1px; }
  .card--front .brand-mark__tag { font-size: 21px; letter-spacing: 1px; margin-top: 3px; }

  .service-band {
    position: absolute;
    left: 0; right: 0; top: 356px; height: 48px;
    background: var(--band-teal);
    display: flex; align-items: center; justify-content: center;
    font-family: "Montserrat", sans-serif;
    font-weight: 500;
    font-size: 19px;
    color: #fff;
    letter-spacing: 0.5px;
  }
  .service-band__item { padding: 0 12px; }
  .service-band__divider { width: 2px; height: 24px; background: #fff; }

  .back-art { position: absolute; left: 0; top: 0; }

  .holder {
    position: absolute; right: 42px; top: 46px; text-align: right;
  }
  .holder__name {
    font-family: "Montserrat", sans-serif; font-weight: 600;
    font-size: 27px; color: var(--ink); line-height: 1.2;
  }
  .holder__title { font-size: 15px; color: var(--ink); margin-top: 4px; }

  .card--back .brand-mark { left: 40px; right: auto; width: 280px; top: 150px; }
  .card--back .brand-mark__dot { width: 62px; height: 62px; margin-bottom: 70px; }
  .card--back .brand-mark__name { font-size: 32px; letter-spacing: 0.5px; }
  .card--back .brand-mark__tag { font-size: 16px; letter-spacing: 0.5px; margin-top: 3px; }

  .contact {
    position: absolute; left: 376px; top: 218px;
    list-style: none; color: var(--brand-blue); font-size: 17px;
  }
  .contact__row { display: flex; align-items: center; height: 27px; }
  .contact__icon { width: 18px; height: 18px; margin-right: 18px; fill: var(--brand-blue); }
  .contact__address { margin-top: 14px; }
</style>
</head>
<body>

  <section class="card card--front">
    <div class="scene-placeholder" role="img" aria-label="Illustrated tropical beach with blue sky, white clouds, turquoise sea and golden sand"></div>
    <div class="brand-mark">
      <span class="brand-mark__dot"></span>
      <span class="brand-mark__name">BRIGHTWAVE</span>
      <span class="brand-mark__tag">TRAVEL AND TOURS</span>
    </div>
    <div class="service-band">
      <span class="service-band__item">Hotel Reservations</span>
      <span class="service-band__divider"></span>
      <span class="service-band__item">Airline Ticketing</span>
      <span class="service-band__divider"></span>
      <span class="service-band__item">Day Tour</span>
    </div>
  </section>

  <section class="card card--back">
    <svg class="back-art" width="711" height="415" viewBox="0 0 711 415">
      <path role="img" aria-label="Beach scene strip with sky, sea and sand"
            d="M0,0 H711 V186 C640,176 590,132 520,94 C400,30 220,30 60,62 L0,40 Z"
            fill="var(--strip-fill)"/>
      <path d="M0,40 C140,8 300,0 420,36 C330,20 180,30 0,72 Z"
            fill="var(--swoosh-light)"/>
      <path d="M60,62 C220,30 400,38 520,100 C600,140 650,178 711,186 V182 C640,172 590,130 520,92 C400,28 220,28 60,62 Z"
            fill="var(--swoosh-dark)" stroke="var(--swoosh-dark)" stroke-width="4"/>
    </svg>

    <div class="holder">
      <div class="holder__name">Your name</div>
      <div class="holder__title">Your Title</div>
    </div>

    <div class="brand-mark">
      <span class="brand-mark__dot"></span>
      <span class="brand-mark__name">BRIGHTWAVE</span>
      <span class="brand-mark__tag">TRAVEL AND TOURS</span>
    </div>

    <ul class="contact">
      <li class="contact__row">
        <svg class="contact__icon" viewBox="0 0 24 24"><path d="M3 9c0-3 4-5 9-5s9 2 9 5v2h-5V9H8v2H3z M6 12h12l2 8H4z"/></svg>
        +00 111 222 3333
      </li>
      <li class="contact__row">
        <svg class="contact__icon" viewBox="0 0 24 24"><path d="M2 5h20v14H2z M4 7l8 6 8-6" fill="none" stroke="var(--brand-blue)" stroke-width="2.4"/></svg>
        yourname@yourwebsite.com
      </li>
      <li class="contact__row">
        <svg class="contact__icon" viewBox="0 0 24 24"><g fill="none" stroke="var(--brand-blue)" stroke-width="1.8"><circle cx="12" cy="12" r="9"/><ellipse cx="12" cy="12" rx="4" ry="9"/><path d="M3 12h18M5 7h14M5 17h14"/></g></svg>
        www.yourwebsite.com
      </li>
      <li class="contact__address">Your Long hotel Address with pincode</li>
    </ul>
  </section>

</body>
</html>
```